TLA marine wildlife conservation strategy

The Coastal Habitat Alliance (tla-reefs.org) needs an illustration to explain in a captivating and clear fashion the influences and interactions underlying our marine wildlife conservation planning and policymaking process. This will be included in our forthcoming strategy paper, and widely presented in conferences. Ultimately, this illustration will help governments take the right decisions to protect wildlife and natural resources.
Guidelines:
Size: The illustration shall fit in a A4 page, and also render nicely on a projector screen (1920x1080)
Colors: Avoid too colorful and 'playful' color code
Text: - Case shall be consistent throughout the graphic (unlike the draft design provided)
Graphic elements:
- In the top right of the graphic there is supposed to be a map of Myanmar. The map is attached. Feel free to adjust the map colors and style to match the illustration.
The only key areas we shall include in the map are:
- Myanmar borders
- EEZ (green),
- state/region borders (dotted lines),
- two marine corridors (blue and light red).
Everything else shall be left out (such as minimap, legend, scale, compass, SEZ).
- On the bottom right, it's important for the national benefits to be presented as a Venn diagram like in the original draft illustration (three intersecting circles)
Any questions? Please ask: dmarsh@tla-reefs.org
Thank you!
Target Market(s)
Scientists, policy makers.
Industry/Entity Type
Environment

```html
<!DOCTYPE html>
<html lang="en">
<head>
<meta charset="utf-8">
<title>TLA Marine Spatial Planning Framework</title>
<link href="https://fonts.googleapis.com/css2?family=Oswald:wght@400;500&family=Titillium+Web:wght@400;600;700&display=swap" rel="stylesheet">
<style>
  :root {
    --bg: #f2f2f2;
    --ink: #333333;
    --white: #ffffff;
    --leaf: #7ab648;
    --ring-top: #3c90ba;
    --ring-right: #2a6f93;
    --ring-left: #86b9d6;
    --teal: #23958c;
    --sky: #4a9cc4;
    --orange: #f4a424;
    --map-sea: #cfe3ec;
    --map-land: #8fc45f;
  }
  * { margin: 0; padding: 0; box-sizing: border-box; }
  html, body { width: 1200px; height: 848px; overflow: hidden; background: var(--bg); }
  .canvas { position: relative; width: 1200px; height: 848px; font-family: "Titillium Web", sans-serif; color: var(--ink); }
  .diagram { position: absolute; inset: 0; }
  .driver {
    position: absolute; display: flex; align-items: center; justify-content: center; text-align: center;
    background: var(--leaf); color: var(--white); font-size: 17px; line-height: 1.25; font-weight: 600;
    border: 2px solid var(--ink); border-radius: 9px; box-shadow: inset 0 0 0 4px var(--white); padding: 8px 14px;
  }
  .driver--politics { left: 342px; top: 46px; width: 327px; height: 45px; }
  .driver--growth { left: 31px; top: 131px; width: 242px; height: 100px; }
  .driver--coordination { left: 31px; top: 325px; width: 208px; height: 105px; }
  .driver--decline { left: 384px; top: 707px; width: 248px; height: 106px; }
  .sector-list { position: absolute; left: 62px; top: 478px; list-style: none; }
  .sector { height: 59.5px; display: flex; align-items: center; font-size: 17px; font-weight: 600; padding-left: 46px; }
  .map-title {
    position: absolute; left: 900px; top: 78px; font-family: "Oswald", sans-serif; font-weight: 500;
    font-size: 26px; line-height: 1.1; letter-spacing: 1px; color: var(--ink);
  }
  .benefits-title {
    position: absolute; left: 758px; top: 636px; font-family: "Oswald", sans-serif; font-weight: 500;
    font-size: 28px; line-height: 1.1; letter-spacing: 1px;
  }
  .venn-label { position: absolute; font-size: 17px; font-weight: 600; line-height: 1.2; text-align: center; }
  .venn-label--economic { left: 848px; top: 560px; width: 110px; }
  .venn-label--social { left: 850px; top: 786px; width: 110px; }
  .venn-label--environment { left: 1050px; top: 786px; width: 140px; }
</style>
</head>
<body>
<main class="canvas">
  <svg class="diagram" width="1200" height="848" viewBox="0 0 1200 848" xmlns="http://www.w3.org/2000/svg">
    <defs>
      <path id="arc-top-outer" d="M332.5,348.9 A240 240 0 0 1 783.5,348.9"/>
      <path id="arc-top-inner" d="M358.8,358.5 A212 212 0 0 1 757.2,358.5"/>
      <path id="arc-right-outer" d="M794.7,367.6 A245 245 0 0 1 536.6,675.1"/>
      <path id="arc-right-inner" d="M765.7,375.4 A215 215 0 0 1 539.3,645.2"/>
      <path id="arc-left" d="M499.8,648.3 A225 225 0 0 1 340.7,372.8"/>
      <path id="arc-stakeholder" d="M385,431 A173 173 0 1 1 731,431 A173 173 0 1 1 385,431"/>
      <path id="arc-vision" d="M463,364.5 A116 116 0 0 1 653,364.5"/>
      <path id="arc-coordination" d="M672.2,410.9 A116 116 0 0 1 558,547"/>
      <path id="arc-decision" d="M509,536 A116 116 0 0 1 452.9,382"/>
    </defs>

    <!-- connectors from drivers -->
    <g class="connectors" stroke="var(--ink)" stroke-width="2" fill="var(--leaf)">
      <line x1="660" y1="91" x2="669" y2="116"/>
      <polygon points="662,114 678,110 674,128"/>
      <line x1="273" y1="168" x2="328" y2="188"/>
      <polygon points="322,180 341,193 320,197"/>
      <line x1="239" y1="342" x2="258" y2="330"/>
      <polygon points="252,323 272,322 262,338"/>
      <line x1="430" y1="707" x2="430" y2="676"/>
      <polygon points="421,679 430,661 439,679"/>
    </g>

    <!-- outer ring -->
    <g class="outer-ring" stroke="var(--white)" stroke-width="3">
      <path fill="var(--ring-top)" d="M304.3,338.7 A270 270 0 0 1 811.7,338.7 L741.2,364.3 A195 195 0 0 0 374.8,364.3 Z"/>
      <path fill="var(--ring-right)" d="M811.7,338.7 A270 270 0 0 1 511.1,696.9 L524.1,623 A195 195 0 0 0 741.2,364.3 Z"/>
      <path fill="var(--ring-left)" d="M511.1,696.9 A270 270 0 0 1 304.3,338.7 L374.8,364.3 A195 195 0 0 0 524.1,623 Z"/>
    </g>
    <g class="ring-labels" fill="var(--white)" font-family="Titillium Web, sans-serif" font-weight="700" font-size="21" text-anchor="middle">
      <text><textPath href="#arc-top-outer" startOffset="50%">Consensus Building and</textPath></text>
      <text><textPath href="#arc-top-inner" startOffset="50%">Capacity Development</textPath></text>
      <text><textPath href="#arc-right-outer" startOffset="50%">Development of</textPath></text>
      <text><textPath href="#arc-right-inner" startOffset="50%">Institutional Arrangements</textPath></text>
      <text><textPath href="#arc-left" startOffset="50%">Data Knowledge Strengthening</textPath></text>
    </g>

    <!-- stakeholder ring -->
    <circle cx="558" cy="431" r="194" fill="var(--white)"/>
    <circle cx="558" cy="431" r="155" fill="none" stroke="var(--ring-top)" stroke-width="2"/>
    <g class="stakeholder-labels" fill="var(--ink)" font-family="Titillium Web, sans-serif" font-size="13" text-anchor="middle">
      <text><textPath href="#arc-stakeholder" startOffset="28%">Stakeholder Engagement</textPath></text>
      <text><textPath href="#arc-stakeholder" startOffset="55%">Stakeholder Engagement</textPath></text>
      <text><textPath href="#arc-stakeholder" startOffset="90%">Stakeholder Engagement</textPath></text>
    </g>

    <!-- process cycle -->
    <g class="cycle">
      <path d="M458.1,361 A122 122 0 0 1 657.9,361" fill="none" stroke="var(--teal)" stroke-width="36"/>
      <polygon points="639.9,373.6 676,348.4 670.3,383.3" fill="var(--teal)"/>
      <path d="M678.1,409.8 A122 122 0 0 1 558,553" fill="none" stroke="var(--sky)" stroke-width="36"/>
      <polygon points="558,531 558,575 532.6,550.3" fill="var(--sky)"/>
      <path d="M506.4,541.6 A122 122 0 0 1 447.4,379.4" fill="none" stroke="var(--leaf)" stroke-width="36"/>
      <polygon points="467.4,388.7 427.5,370.1 460.6,357.6" fill="var(--leaf)"/>
    </g>
    <g class="cycle-labels" fill="var(--white)" font-family="Titillium Web, sans-serif" font-weight="700" font-size="15" text-anchor="middle">
      <text><textPath href="#arc-vision" startOffset="50%">Shared Vision</textPath></text>
      <text><textPath href="#arc-coordination" startOffset="50%">Coordination</textPath></text>
      <text><textPath href="#arc-decision" startOffset="50%">Decision Support</textPath></text>
    </g>
    <circle cx="558" cy="431" r="80" fill="var(--white)" stroke="var(--ink)" stroke-width="2"/>
    <g class="core-label" fill="var(--ink)" font-family="Oswald, sans-serif" font-weight="500" font-size="24" text-anchor="middle">
      <text x="558" y="408">Marine</text>
      <text x="558" y="440">Spatial</text>
      <text x="558" y="472">Planning</text>
    </g>

    <!-- adaptive management -->
    <polygon points="719,304 746,276 746,286 884,286 884,276 911,304" fill="var(--teal)"/>
    <polygon points="719,304 911,304 884,332 884,322 746,322 746,332" fill="var(--leaf)"/>
    <g fill="var(--white)" font-family="Titillium Web, sans-serif" font-weight="700" font-size="13" text-anchor="middle">
      <text x="812" y="300">Adaptive</text>
      <text x="812" y="318">Management</text>
    </g>

    <!-- plan sheet -->
    <path d="M854,43 H1170 V475 L1130,515 H854 Z" fill="var(--white)" stroke="var(--ink)" stroke-width="3"/>
    <path d="M1130,515 L1136,480 L1170,475 Z" fill="#d8d8d8" stroke="var(--ink)" stroke-width="2"/>
    <rect x="880" y="185" width="270" height="300" rx="6" fill="url(#map-tone)" role="img" aria-label="Map of Myanmar showing national borders, the exclusive economic zone in green, dotted state and region borders, and two marine corridors"/>
    <linearGradient id="map-tone" x1="0" y1="0" x2="1" y2="1">
      <stop offset="0" stop-color="var(--map-sea)"/>
      <stop offset="1" stop-color="var(--map-land)"/>
    </linearGradient>

    <path d="M1168,520 C1185,570 1180,615 1160,648" fill="none" stroke="var(--ink)" stroke-width="3" stroke-dasharray="9 7"/>
    <polygon points="1148,640 1170,640 1154,664" fill="var(--ink)"/>

    <!-- sector list -->
    <line x1="33" y1="430" x2="33" y2="792" stroke="var(--ink)" stroke-width="2"/>
    <g class="bullets" fill="var(--leaf)" stroke="var(--ink)" stroke-width="2">
      <circle cx="33" cy="495" r="5"/><circle cx="33" cy="554" r="5"/><circle cx="33" cy="614" r="5"/>
      <circle cx="33" cy="673" r="5"/><circle cx="33" cy="733" r="5"/><circle cx="33" cy="792" r="5"/>
    </g>
    <g class="sector-icons" stroke="var(--ink)" stroke-width="2" fill="var(--ring-left)" stroke-linejoin="round">
      <rect x="56" y="482" width="30" height="22" rx="4"/>
      <path d="M59,498 q5,-5 10,0 t10,0 t6,-2" fill="none"/>
      <path d="M71,538 q-7,9 0,13 q7,-4 0,-13 Z"/>
      <path d="M55,560 q10,-4 18,2 h10 l4,-4" fill="none"/>
      <path d="M55,612 h34 l-5,9 h-24 Z"/>
      <rect x="64" y="603" width="16" height="9"/>
      <path d="M57,672 q14,-12 26,0 q-12,12 -26,0 Z"/>
      <path d="M83,672 l7,-6 v12 Z"/>
      <path d="M56,738 h32 l-4,6 h-24 Z"/>
      <path d="M66,738 l4,-20 l4,20 M80,738 v-14 l6,-6" fill="none"/>
      <path d="M55,795 h34 l-5,8 h-24 Z"/>
      <rect x="62" y="783" width="20" height="12"/>
      <rect x="68" y="776" width="8" height="7"/>
    </g>

    <!-- national benefits -->
    <line x1="743" y1="640" x2="743" y2="804" stroke="var(--ink)" stroke-width="2"/>
    <g class="venn" stroke="var(--ink)" stroke-width="2" style="mix-blend-mode:multiply">
      <circle cx="1020" cy="625" r="64" fill="var(--ring-left)" fill-opacity="0.85"/>
      <circle cx="958" cy="718" r="66" fill="var(--orange)" fill-opacity="0.85"/>
      <circle cx="1082" cy="718" r="66" fill="var(--leaf)" fill-opacity="0.85"/>
    </g>
    <g stroke="var(--ink)" stroke-width="2">
      <line x1="930" y1="598" x2="1000" y2="630"/>
      <line x1="912" y1="782" x2="950" y2="740"/>
      <line x1="1112" y1="782" x2="1085" y2="742"/>
    </g>
  </svg>

  <div class="driver driver--politics">Political Transition</div>
  <div class="driver driver--growth">Increasing Development Pressures from Rapid Economic Growth</div>
  <div class="driver driver--coordination">Weak Coordination Between Marine Sectors</div>
  <div class="driver driver--decline">Declining Marine and Coastal Ecosystems and Resources</div>

  <ul class="sector-list">
    <li class="sector">Coastal Tourism</li>
    <li class="sector">Marine &amp; Coastal Conservation</li>
    <li class="sector">Navy &amp; Marine Police</li>
    <li class="sector">Marine Fisheries</li>
    <li class="sector">Offshore Gas &amp; Exploration</li>
    <li class="sector">Marine Transport</li>
  </ul>

  <div class="map-title">Spatial<br>Management<br>Plan</div>
  <div class="benefits-title">National<br>Benefits</div>
  <div class="venn-label venn-label--economic">Economic<br>Value</div>
  <div class="venn-label venn-label--social">Social<br>Development</div>
  <div class="venn-label venn-label--environment">Environmental<br>Sustainability</div>
</main>
</body>
</html>
```